Create a Brochure Design for Harlow Senior Living

Harlow Senior Living is a subsidiary of the Harlow Care Group. This brochure is specifically for the Harlow Senior Living company and brand. Create a 3 panel, front and back, tri-fold brochure. This brochure will be a way to introduce our senior living care home to the community, prospective, clients, and various referral partners. It is modern and state of the art home. Like the home, the brochure must be eye catching, unique in its deliverables (as it doesn’t feel like a care facility) and demonstrate both attention to detail and comfort. Our organization is sophisticated and built around warmth, care and individualized personal attention. The most important aspect of this design is to focus on creating a nurturing, warm, and inviting feel where you would want to put your own loved ones in our care home.
I am open to the creativity of the designer to develop something based on the above criteria; however I would like the design to work well with the existing collateral material. What I mean by that is that while I want everything to have its own personality and stand out as its own brand representative, I still need to be able to tell that the overall design concept stays stylistically inside of the same ‘family’ of existing designed material. Because of this, below I would like for the designer to pull inspiration from the link to our website (Located below) as well as from the attachment of our recently refreshed business cards (Attached). This should allow each design to be unique and creative, while still staying inside of a framework and the feel/style that I am looking for.
Finally, I want all the designers to understand that this brochure design is for a facility where we are responsible to provide care for active, positive, and happy seniors/elders. We have care professionals and staff on-site to provide 24x7, around the clock, care to the elders and geriatric residents as it is needed and required. The photos that are used must represent aging gracefully and with elegance.
Target Market(s)
Seniors(50+), Caring Family Members, Social Workers, Physicians, Hospitals
Industry/Entity Type
Business
Requirements
Must have
- • The company logo must be included.
Nice to have
- Attached you will find a sampling of images related to the long term care industry. Please feel free to use your own images as you see fit. The interior care home pictures are of our actual facility and should be incorporated into the brochure and your design.
Company Information
• Look under the Harlow Senior Living tab at
www.harlowcaregroup.example.

```html
<!DOCTYPE html>
<html lang="en">
<head>
<meta charset="utf-8">
<title>Harlow Senior Living – Tri-fold Brochure</title>
<link rel="stylesheet" href="https://fonts.googleapis.com/css2?family=EB+Garamond:ital,wght@0,400;0,600;0,700;1,600&display=swap">
<style>
  :root {
    --backdrop: #e4e4e4;
    --paper: #d7ccb6;
    --paper-shade: #cdc1a9;
    --teal: #4f9995;
    --teal-light: #5fa8a3;
    --ink: #3f3b36;
    --ink-soft: #55504a;
    --cream: #f7f2e8;
  }
  * { margin: 0; padding: 0; box-sizing: border-box; }
  html, body { width: 1200px; height: 916px; overflow: hidden; }
  body {
    background: radial-gradient(ellipse at 50% 45%, #f2f2f2 0%, var(--backdrop) 70%, #d6d6d6 100%);
    font-family: "EB Garamond", Georgia, serif;
    color: var(--ink);
    position: relative;
  }
  .brochure {
    position: absolute;
    left: 45px; top: 78px;
    width: 1110px; height: 760px;
    background: var(--paper);
    box-shadow: 0 10px 30px rgba(0,0,0,0.18);
    display: flex;
    overflow: hidden;
  }
  .panel {
    position: relative;
    width: 370px; height: 760px;
  }
  .panel + .panel { border-left: 1px solid rgba(120,105,80,0.18); }

  /* Left panel – story */
  .story { padding: 26px 26px 0 28px; }
  .story-title {
    font-style: italic; font-weight: 600;
    font-size: 24px; color: var(--cream);
    margin-bottom: 10px;
  }
  .story-copy p {
    font-size: 13.4px; line-height: 17px;
    text-align: justify; color: var(--ink);
    margin-bottom: 9px;
  }
  .photo { position: absolute; left: 0; bottom: 0; }

  /* Middle panel */
  .brand-mark {
    display: flex; flex-direction: column; align-items: center; gap: 8px;
  }
  .brand-mark .square { width: 30px; height: 30px; background: var(--teal); border-radius: 5px; }
  .brand-mark .name { color: var(--teal); font-weight: 400; text-align: center; line-height: 1.05; }
  .middle .brand-mark { margin-top: 46px; }
  .middle .brand-mark .name { font-size: 26px; }
  .mission {
    margin: 26px 36px 0;
    font-size: 13.6px; line-height: 17px; text-align: center; color: var(--ink);
  }
  .mission p + p { margin-top: 6px; }
  .map {
    position: absolute; left: 40px; top: 300px;
    width: 290px; height: 210px;
    background: linear-gradient(135deg, #e3dccd 0%, #d9cfbc 50%, #e6dfd0 100%);
    border-radius: 3px;
  }
  .contact {
    position: absolute; left: 0; bottom: 0; width: 370px; height: 250px;
  }
  .contact-text {
    position: absolute; left: 0; top: 30px; width: 100%;
    text-align: center; color: var(--cream);
  }
  .contact-title { font-weight: 700; font-size: 20px; margin-bottom: 6px; }
  .contact-lines { font-size: 17px; line-height: 22px; font-style: normal; }

  /* Right panel – cover */
  .cover { text-align: center; }
  .cover-group { margin-top: 44px; font-weight: 700; font-size: 23px; color: var(--ink-soft); }
  .cover-intro { font-size: 18px; color: var(--cream); margin-top: 2px; }
  .cover-headline { font-weight: 700; font-size: 27px; color: var(--teal); line-height: 30px; margin-top: 4px; }
  .cover .brand-mark { margin-top: 32px; }
  .cover .brand-mark .square { width: 54px; height: 54px; border-radius: 9px; }
  .cover .brand-mark .name { font-size: 40px; }
  .features { margin-top: 30px; }
  .features .lead { font-weight: 700; font-size: 17px; color: var(--ink); }
  .features li { list-style: none; font-size: 17px; color: var(--ink); margin-top: 6px; }
  .features li small { font-size: 14px; }
</style>
</head>
<body>
  <main class="brochure">

    <section class="panel story">
      <h2 class="story-title">The Harlow Story</h2>
      <div class="story-copy">
        <p>The time will come when we will all have to reach out for help. It might happen after a sudden, unexpected visit to the hospital. Or it could occur after 70 years where you “never had a single sick day in your life.”</p>
        <p>When you reach out, Harlow Homecare will be there.</p>
        <p>Harlow is more than a home care provider. We’re somebody you can depend on without question.</p>
        <p>We understand what it means to need help. We understand how hard it is to ask. And we understand the bewildering number of choices we all face when we’re confronted with the need for health care.</p>
        <p>We want you to know that you don’t have to do it alone. Whether you need help in caring for yourself, or you need to find someone who you can entrust with the care of your husband or wife, your parents or your child… we’re here to help. Our services are the benchmark for the homecare industry because of the passion that we bring to recruiting, testing, training, motivating and supervising the people who care for our clients.</p>
      </div>
      <svg class="photo" width="370" height="230" viewBox="0 0 370 230" role="img" aria-label="Photo of the garden walkway and veranda outside the home">
        <defs>
          <linearGradient id="garden" x1="0" y1="0" x2="1" y2="1">
            <stop offset="0" stop-color="#4f6b36"/>
            <stop offset="0.5" stop-color="#7d8a5c"/>
            <stop offset="1" stop-color="#b9b1a0"/>
          </linearGradient>
        </defs>
        <path d="M0 30 Q120 0 240 18 T370 40 V230 H0 Z" fill="url(#garden)"/>
      </svg>
    </section>

    <section class="panel middle">
      <div class="brand-mark">
        <span class="square"></span>
        <span class="name">Harlow<br>Senior Living</span>
      </div>
      <div class="mission">
        <p>This is more than a job for us. Some people devote their lives to teaching, some to science.</p>
        <p>For us, it’s caring for you or your family member. Our job is simply to make your job easier.</p>
      </div>
      <div class="map" role="img" aria-label="Street map showing the location of the home"></div>
      <div class="contact">
        <svg width="370" height="250" viewBox="0 0 370 250" aria-hidden="true">
          <path d="M0 14 Q185 -8 370 14 V250 H0 Z" fill="var(--teal)"/>
        </svg>
        <div class="contact-text">
          <h3 class="contact-title">Contact Us</h3>
          <address class="contact-lines">
            Harlow Homecare<br>
            480 Lanikai Way<br>
            Suite #210<br>
            Honolulu, HI 96813<br>
            Phone: 808-555-0142<br>
            Fax: 808-555-0187<br>
            info@harlowcare.example
          </address>
        </div>
      </div>
    </section>

    <section class="panel cover">
      <p class="cover-group">The Harlow Care Group</p>
      <p class="cover-intro">proudly introduces</p>
      <h1 class="cover-headline">a new era in<br>Senior Living</h1>
      <div class="brand-mark">
        <span class="square"></span>
        <span class="name">Harlow<br>Senior Living</span>
      </div>
      <ul class="features">
        <li class="lead">The brand new, state of the art home</li>
        <li>19 private rooms <small>with bathrooms</small></li>
        <li>Staff is on-hand 24/7</li>
      </ul>
      <svg class="photo" width="370" height="250" viewBox="0 0 370 250" role="img" aria-label="Photo of a bright private bedroom in the home">
        <defs>
          <linearGradient id="bedroom" x1="0" y1="0" x2="1" y2="1">
            <stop offset="0" stop-color="#7a5a3a"/>
            <stop offset="0.45" stop-color="#d9b98a"/>
            <stop offset="1" stop-color="#efe2b8"/>
          </linearGradient>
        </defs>
        <path d="M0 26 Q180 -6 370 30 V250 H0 Z" fill="url(#bedroom)"/>
      </svg>
    </section>

  </main>
</body>
</html>
```